Calling All Web Design Visionaries: Transform the Vantic Harbor Website!

Dear Web Design Innovators,

Are you ready to embark on a cosmic design journey? We are thrilled to announce an exciting opportunity to revamp and upgrade the Vantic Harbor website, and we need your exceptional design prowess to bring our vision to life.

About Vantic Harbor:
Vantic Harbor is on a mission to reshape the future of space construction. We're pioneers in the field, developing cutting-edge concept construction blocks that promise to redefine how we build beyond our planet's boundaries. Our solutions are scalable, sustainable, and poised to accelerate humanity's journey into the cosmos.

Current Website:
Take a look at our current website [www.vanticharbor-example.co.uk](https://www.vanticharbor-example.co.uk) to get a glimpse of our existing online presence. While it served us well, we believe it's time for a transformative makeover.

Your Mission:
We're seeking imaginative web designers who can bring a fresh perspective to our online platform. Here's the website layout we're envisioning:
- Homepage: A futuristic and clean design that reflects our commitment to innovation. Clear navigation to key sections.
- About Us: A captivating section introducing our mission and team.
- Products: Highlighting our revolutionary concept construction blocks.
- Projects: Showcasing our involvement in space construction initiatives.
- Blog: A space to share our insights, progress, and news.
- Contact: Easy access for potential partners and investors to reach out.

Image Suggestions:
- Celestial imagery, cosmic landscapes, and space construction concepts can add a captivating visual element.
- Incorporate a color palette that combines deep space blues with modern metallic tones for a futuristic feel.
- Use high-quality images and graphics that convey the excitement and possibilities of space construction.

Why You Should Join Us:
By taking on this challenge, you'll have the chance to contribute to a groundbreaking mission and be part of the future of space exploration. Your design will be seen by space enthusiasts, investors, and industry experts worldwide.

If you're ready to embark on this cosmic design journey with us, please submit your portfolio and a brief introduction by 22/09/23. We can't wait to see your visionary concepts.

Let's transform the Vantic Harbor website into a space of inspiration and innovation. Join us on this incredible adventure!

Best regards,

Ned

Target Market(s)

Orbit Service providers, Governments, Space Agencies. Space Infrastructure

Industry/Entity Type

Space, Technology, Innovation, Architecture. Construction

Coding

Coded - Design and coding required

Number of Pages Required

5+ page

Colors
0054AA
0677BA
7BADD7
CADEEF
E8F1F8
6B429C
8869AF
B7A5CE
E3DAEB
F3F0F8

Requirements
Must have
• The logos i have outlined in the website revamp doc, i also need a sub section for FAQs terms of service etc like most professional websites. A page to sell merch. Like our custom hoody, t shirt, key rings, hats, joggers, etc
Nice to have
• any case studies of satellite innovations reaching project completion and how they might relate to my project.

```html
<!DOCTYPE html>
<html lang="en">
<head>
<meta charset="utf-8">
<title>Vantic Harbor — Invest in the Future</title>
<link href="https://fonts.googleapis.com/css2?family=Saira+Condensed:wght@300;400;500;700&display=swap" rel="stylesheet">
<style>
  :root {
    --space-black: #02040a;
    --space-navy: #06102a;
    --deep-blue: #0b2a6b;
    --glow-blue: #2f6fd6;
    --accent-blue: #2b35f5;
    --nav-active: #3a44ff;
    --text-white: #ffffff;
    --text-soft: #dfe6f3;
    --badge-red: #7a1d1d;
    --band-tone: #0a0d16;
  }
  * { box-sizing: border-box; margin: 0; padding: 0; }
  html, body {
    width: 1200px; height: 960px; overflow: hidden;
    background: var(--space-black);
    font-family: "Saira Condensed", "Arial Narrow", sans-serif;
    color: var(--text-white);
  }
  .page { position: relative; width: 1200px; height: 960px; }

  .hero { position: absolute; inset: 0 0 160px 0; overflow: hidden; }
  .hero-backdrop {
    position: absolute; inset: 0;
    background:
      radial-gradient(ellipse 300px 90px at 600px 500px, rgba(120,170,255,.55), transparent 70%),
      radial-gradient(ellipse 420px 300px at 610px 820px, #1c4f9a 0%, #0f2f66 45%, transparent 72%),
      radial-gradient(ellipse 700px 380px at 600px 480px, rgba(47,111,214,.35), transparent 70%),
      linear-gradient(180deg, var(--space-black) 0%, var(--space-navy) 55%, var(--deep-blue) 100%);
  }

  .site-header {
    position: absolute; top: 44px; left: 70px; right: 60px;
    display: flex; align-items: center; justify-content: space-between;
  }
  .brand { display: flex; align-items: center; gap: 12px; }
  .brand-dot { width: 34px; height: 34px; border-radius: 50%; background: #b9c0cc; }
  .brand-name { font-size: 30px; font-weight: 500; color: #c9ced8; letter-spacing: .02em; }

  .main-nav { display: flex; align-items: center; gap: 36px; margin-top: 80px; }
  .main-nav a {
    color: var(--text-white); text-decoration: none;
    font-size: 15px; font-weight: 500; text-transform: uppercase; letter-spacing: .03em;
  }
  .main-nav a.is-active { color: var(--nav-active); }
  .search-pill {
    display: flex; align-items: center; gap: 6px;
    border: 1.5px solid var(--text-white); border-radius: 20px;
    padding: 6px 16px; font-size: 14px; color: var(--text-white);
  }

  .hero-content {
    position: absolute; top: 250px; left: 0; right: 0;
    text-align: center;
  }
  .hero-title {
    font-family: "Saira Condensed", "Arial Narrow", sans-serif;
    font-weight: 700; font-size: 66px; line-height: 1; text-transform: uppercase;
    letter-spacing: .005em;
  }
  .hero-subtitle { margin-top: 20px; font-size: 40px; font-weight: 400; line-height: 1.1; }
  .hero-text {
    margin: 22px auto 0; max-width: 480px;
    font-size: 19px; line-height: 1.3; font-weight: 300; color: var(--text-soft);
  }
  .btn-primary {
    display: inline-flex; align-items: center; gap: 10px;
    margin-top: 30px; padding: 14px 20px;
    background: var(--accent-blue); color: var(--text-white);
    font-size: 16px; font-weight: 500; text-decoration: none; border-radius: 2px;
  }

  .hero-badge {
    position: absolute; left: 990px; top: 540px;
    width: 90px; height: 90px; border-radius: 50%;
    background: var(--badge-red); opacity: .85;
  }

  .intro-band {
    position: absolute; left: 0; right: 0; bottom: 0; height: 160px;
    background: var(--space-black); overflow: hidden;
  }
  .intro-visual {
    position: absolute; left: 480px; top: 40px; width: 240px; height: 120px;
    background: radial-gradient(ellipse at 50% 100%, #1a1f2c 0%, var(--band-tone) 70%);
  }
</style>
</head>
<body>
<div class="page">
  <section class="hero">
    <div class="hero-backdrop" role="img" aria-label="Starfield over the night side of Earth with a rising blue sunrise glow"></div>

    <header class="site-header">
      <div class="brand">
        <span class="brand-dot"></span>
        <span class="brand-name">Vantic Harbor</span>
      </div>
      <nav class="main-nav">
        <a href="#" class="is-active">Home</a>
        <a href="#">About Us</a>
        <a href="#">Products</a>
        <a href="#">Projects</a>
        <a href="#">Blog</a>
        <a href="#">Contact</a>
        <span class="search-pill">
          <svg width="12" height="12" viewBox="0 0 12 12" fill="none" stroke="#fff" stroke-width="1.6"><circle cx="5" cy="5" r="3.8"/><path d="M8 8l3 3"/></svg>
          Search
        </span>
      </nav>
    </header>

    <div class="hero-content">
      <h1 class="hero-title">Invest in the Future</h1>
      <p class="hero-subtitle">Dare to Dream, Dare to Invest</p>
      <p class="hero-text">A new frontier beckons, and it's unlike anything humanity has ever witnessed. The possibilities are boundless, the horizons limitless. Are you ready to join the voyage into the future?</p>
      <a href="#" class="btn-primary">Learn More
        <svg width="8" height="12" viewBox="0 0 8 12" fill="none" stroke="#fff" stroke-width="1.8"><path d="M2 1l5 5-5 5"/></svg>
      </a>
    </div>

    <div class="hero-badge" aria-hidden="true"></div>
  </section>

  <section class="intro-band">
    <div class="intro-visual" role="img" aria-label="Dashed line illustration of a globe with an orbit path"></div>
  </section>
</div>
</body>
</html>
```